Designer Needed for Protein Label

We are looking for an experienced graphic designer to create a label for our protein supplement Quill ISOLATE 100% WHEY Protein 3LB tub. You can make it unique to our design but keep it clean and simple.

Here are some design examples that we liked, however please note ours is unflavored:

https://www.brantova.com/VelnorFit-Tundra-Protein-Powder-Chocolate/dp/K47RQWZ2NX/ref=sr_1_17_a_it?ie=UTF8&qid=1536255229&sr=8-17&keywords=protein%2Bpowder&th=1

https://www.brantova.com/dp/K93TLMQ5VB/ref=sspa_dk_detail_1?pd_rd_i=K93TLMQ5VB&pf_rd_m=QWERTYPLMNB&pf_rd_p=7c1402ab-816e-4a2c-9e3f-27a4c188f3d1&pf_rd_r=HJKWPLZNRT8VQC217DMS&pd_rd_wg=TrQ4k&pf_rd_s=desktop-dp-sims&pf_rd_t=40701&pd_rd_w=KLMN3&pf_rd_i=desktop-dp-sims&pd_rd_r=917f3a21-c2de-11e8-942a-ab17fd2249c7&th=1

Please see attachment for Quill Logo and additional label example.

Label Dimensions:
18in x 6in

Please include the following information on the label:
* Quill Icon
* ISOLATE - product name
* 100% WHEY Protein
* Unflavored
* Net WT. 3LB (1.36 KG)
* 40 Servings
* 50 Grams of Protein per serving
* XX  BCAA
* Gluten & Lactose Free
* Kosher and Halal Certified
* Non GMO
* Nutrition Facts (use as place holder)
* Ingredients
* Directions
* Barcode

```html
<!DOCTYPE html>
<html lang="en">
<head>
<meta charset="utf-8">
<title>Quill Isolate 100% Whey Protein – Label Fronts</title>
<link href="https://fonts.googleapis.com/css2?family=Barlow:ital,wght@0,500;0,700;0,800;0,900;1,800;1,900&family=Barlow+Condensed:ital,wght@0,500;0,600;1,500;1,600&display=swap" rel="stylesheet">
<style>
  :root{
    --stage:#ececec;
    --label:#dfdac4;
    --ink:#111111;
    --accent:#f7d117;
    --paper:#ffffff;
  }
  *{box-sizing:border-box;margin:0;padding:0}
  html,body{width:1200px;height:1174px;overflow:hidden;background:var(--stage)}
  .canvas{position:relative;width:1200px;height:1174px}
  .label{position:absolute;top:300px;width:540px;height:575px;background:var(--label);overflow:hidden;
    font-family:"Barlow",sans-serif;color:var(--ink)}
  .label--main{left:50px}
  .label--alt{left:610px}
  .label__band{position:absolute;left:0;top:0;width:100%;height:36px;background:var(--ink)}
  .abs{position:absolute;line-height:1}
  .tagline{font-family:"Barlow Condensed",sans-serif;font-style:italic;font-weight:500;font-size:15px;line-height:1.2;text-transform:uppercase}
  .brand{display:flex;align-items:center;gap:14px}
  .brand__mark{width:40px;height:40px;background:var(--accent)}
  .brand__name{font-family:"Barlow",sans-serif;font-weight:900;font-size:76px;line-height:1;color:var(--ink)}
  .heavy{font-weight:900;letter-spacing:-1px}
  .stats{font-weight:700;font-size:13px;line-height:1.1;text-transform:uppercase;border-left:2px solid var(--ink);padding-left:6px}
  .stats b{display:block;font-weight:800;font-size:26px;line-height:1}
  .certbar{background:var(--ink);color:var(--paper);font-weight:700;font-size:17px;display:flex;align-items:center;justify-content:center;text-transform:uppercase}
  .note{font-family:"Barlow Condensed",sans-serif;font-weight:600;font-size:14px;text-transform:uppercase}
  .pill{border:1.5px solid var(--ink);border-radius:4px;font-family:"Barlow Condensed",sans-serif;font-weight:600;font-size:13px;display:flex;align-items:center;justify-content:center}
  .netbox{background:var(--ink);color:var(--paper);text-align:center;font-weight:800;padding-top:10px}
  .netbox span{display:block;font-size:13px}
  .netbox strong{display:block;font-size:22px}
  .netbox small{display:block;font-size:11px;font-weight:500}
  .netpill{background:var(--ink);color:var(--paper);border-radius:4px;font-weight:700;font-size:12px;display:flex;align-items:center;justify-content:center;gap:3px}
  .netpill strong{font-size:16px}
  .notice{font-family:"Barlow Condensed",sans-serif;font-style:italic;font-weight:500;font-size:12.5px;line-height:1.4;text-transform:uppercase}
  .icon-label{font-weight:700;font-size:8px;text-transform:uppercase;text-align:center;width:50px}
</style>
</head>
<body>
<main class="canvas">

  <section class="label label--main" aria-label="Quill Isolate label, front panel">
    <div class="label__band"></div>
    <p class="abs tagline" style="left:82px;top:56px">With 50 grams of protein from<br>100% whey protein isolate</p>
    <div class="abs brand" style="left:128px;top:100px"><span class="brand__mark"></span><span class="brand__name">Quill</span></div>
    <p class="abs heavy" style="left:82px;top:205px;font-size:54px;font-style:italic">ISOLATE 100%</p>
    <p class="abs heavy" style="left:80px;top:258px;font-size:96px">WHEY</p>
    <p class="abs heavy" style="left:84px;top:348px;font-size:62px;font-weight:800">PROTEIN</p>
    <div class="abs stats" style="left:370px;top:270px;width:150px">
      Per serving<b>50g</b>Protein<br><b style="margin-top:10px">10g</b>BCAA<br>Gluten &amp;<br>Lactose free
    </div>
    <div class="abs certbar" style="left:84px;top:412px;width:390px;height:26px">Non GMO • Kosher and Halal certified</div>

    <svg class="abs" style="left:82px;top:446px" width="160" height="84" viewBox="0 0 160 84" aria-hidden="true">
      <g fill="none" stroke="#111" stroke-width="2.5">
        <polygon points="38,4 72,24 72,60 38,80 4,60 4,24"/>
        <polygon points="120,4 154,24 154,60 120,80 86,60 86,24"/>
      </g>
      <g font-family="Barlow,sans-serif" fill="#111" text-anchor="middle">
        <text x="38" y="42" font-size="20" font-weight="800">50g</text>
        <text x="38" y="55" font-size="10" font-weight="800">PROTEIN</text>
        <text x="38" y="64" font-size="6" font-weight="600">PER SERVING</text>
        <text x="120" y="42" font-size="18" font-weight="800">1.6g</text>
        <text x="120" y="55" font-size="10" font-weight="800">TOTAL FAT</text>
        <text x="120" y="64" font-size="6" font-weight="600">PER SERVING</text>
      </g>
    </svg>

    <p class="abs note" style="left:250px;top:448px">Pure, unflavored</p>
    <svg class="abs" style="left:248px;top:471px" width="150" height="42" viewBox="0 0 150 42" aria-hidden="true">
      <g fill="none" stroke="#111" stroke-width="2.5">
        <circle cx="20" cy="20" r="17"/>
        <circle cx="68" cy="20" r="17"/>
        <circle cx="116" cy="20" r="17"/>
        <path d="M56 20h24M58 14v12M78 14v12M54 17v6M82 17v6"/>
      </g>
      <path d="M112 10h8v6h6v8h-6v6h-8v-6h-6v-8h6z" fill="#111"/>
    </svg>
    <p class="abs icon-label" style="left:243px;top:516px">Muscle</p>
    <p class="abs icon-label" style="left:291px;top:516px">Strength</p>
    <p class="abs icon-label" style="left:339px;top:516px">Recovery</p>

    <div class="abs pill" style="left:402px;top:450px;width:72px;height:18px">Unflavored</div>
    <div class="abs netbox" style="left:402px;top:478px;width:72px;height:97px">
      <span>Net WT.</span><strong>3LB</strong><small>(1.36 KG)</small>
    </div>
  </section>

  <section class="label label--alt" aria-label="Quill Isolate label, alternate front panel">
    <div class="label__band"></div>
    <p class="abs tagline" style="left:82px;top:58px;font-size:21px">Protein powder</p>
    <div class="abs brand" style="left:78px;top:98px"><span class="brand__mark"></span><span class="brand__name">Quill</span></div>
    <p class="abs note" style="left:178px;top:184px;font-weight:500;font-size:17px">Pure naked protein</p>
    <p class="abs heavy" style="left:72px;top:203px;font-size:64px">ISOLATE</p>
    <p class="abs heavy" style="left:78px;top:262px;font-size:92px;font-style:italic">100%</p>
    <p class="abs heavy" style="left:72px;top:352px;font-size:84px">WHEY</p>
    <p class="abs heavy" style="left:82px;top:432px;font-size:60px;font-weight:800">PROTEIN</p>
    <p class="abs notice" style="left:74px;top:498px"><b style="font-weight:700">Notice:</b> use this product as a food supplement only.<br>Do not use for weight reduction.</p>
    <div class="abs netpill" style="left:197px;top:547px;width:122px;height:21px">Net WT.<strong>3LB</strong><span style="font-size:8px;font-weight:500">(1.36 KG)</span></div>
  </section>

</main>
</body>
</html>
```